Trifold - Gentle Horizon Therapy

Marianne Dobbs, Psy.D.Licensed Psychologist

this is for hypnosis and meditation
I like decorative font for my name (conservative decorative)

calming effect is most imortant

Target Market(s)

clients with depression, pain, anxiety - adults and aged

Industry/Entity Type

Conservative

Font styles to use
Serif

Colors
abd037
85cae6
cadf82
34a7d7
ffffff
886aae
6b449b

Requirements
Must have
• I like zen-like calming effects. lime Green, light blues and purple. I like waves and color.
• I like water and light, flowers and plants - bamboo, stacking rocks, ocean, water, lotus flowers
Should not have
• not too much purple
• Mostly green and blue

```html
<!DOCTYPE html>
<html lang="en">
<head>
<meta charset="utf-8">
<title>Gentle Horizon Therapy – Trifold</title>
<link rel="stylesheet" href="https://fonts.googleapis.com/css2?family=Lato:wght@300;400;700&family=Libre+Baskerville:wght@700&family=Dancing+Script:wght@600&display=swap">
<style>
:root{
  --lime:#abd037;
  --lime-soft:#cadf82;
  --sky:#85cae6;
  --blue:#34a7d7;
  --white:#ffffff;
  --lilac:#886aae;
  --purple:#6b449b;
  --ink:#4a4a4a;
  --teal:#1f8fb8;
  --page:#e6e9e3;
}
*{box-sizing:border-box;margin:0;padding:0}
html,body{width:1200px;height:1200px;overflow:hidden;background:var(--page);font-family:'Lato',sans-serif;color:var(--ink)}
.spread{position:absolute;left:30px;width:1140px;height:555px;background:var(--white);box-shadow:0 4px 18px rgba(0,0,0,.18)}
.spread--outside{top:30px}
.spread--inside{top:615px}
.panel{position:absolute;top:0;width:380px;height:555px;overflow:hidden}
.panel + .panel{border-left:1px solid rgba(0,0,0,.06)}
.panel--1{left:0}.panel--2{left:380px}.panel--3{left:760px}
.panel svg.bg{position:absolute;inset:0;width:100%;height:100%}
.layer{position:absolute;inset:0}
.photo{position:absolute}
/* logo */
.logo{display:flex;align-items:center;gap:7px}
.logo__dot{width:22px;height:22px;border-radius:50%;background:var(--lime)}
.logo__name{font-family:'Lato',sans-serif;font-weight:700;font-size:13px;letter-spacing:3px;color:var(--teal);line-height:1}
.logo__name small{display:block;font-size:6.5px;letter-spacing:1.5px;margin-top:2px}
/* services */
.services{position:absolute;left:26px;top:34px;width:330px}
.h-caps{font-family:'Lato',sans-serif;font-weight:700;font-size:13px;color:var(--purple);letter-spacing:.5px;border-bottom:1px solid var(--lilac);padding-bottom:3px;margin-bottom:10px}
.service{display:flex;gap:8px;margin-bottom:12px}
.service__icon{flex:0 0 16px;height:16px;border:1.5px solid var(--blue);border-radius:50%;margin-top:2px}
.service h4{font-size:11px;color:var(--teal);font-weight:700}
.service p{font-size:9.5px;line-height:1.4}
.fee{margin-top:6px;font-size:11px}
.fee b{color:var(--teal)}
.fee strong{display:block;color:#333}
/* back panel */
.back-text{position:absolute;left:20px;right:0;top:250px;text-align:center}
.name-line{font-family:'Lato',sans-serif;font-weight:300;font-size:17px;color:var(--purple)}
.role-line{font-family:'Lato',sans-serif;font-weight:700;font-size:15px;color:var(--purple)}
.mantra{margin-top:10px;font-weight:300;font-size:14px;line-height:1.25;color:var(--teal)}
.contact{margin-top:14px;font-size:10px;line-height:1.4;color:#333}
.contact .icon{display:block;margin:6px auto 3px;width:14px;height:14px}
.contact b{font-weight:700}
/* cover */
.cover-text{position:absolute;left:0;right:0;top:22px;text-align:center}
.cover-text .logo{justify-content:center;margin-bottom:16px}
.tagline{font-family:'Libre Baskerville',serif;font-size:14px;line-height:1.15;color:var(--teal);margin-top:3px}
.tagline span{display:block}
.tagline span:first-child{color:#4f8f1a}
.subline{font-size:10.5px;color:#333;margin-top:5px;line-height:1.3}
.script{font-family:'Dancing Script',cursive;font-size:19px;color:var(--blue);margin-top:8px}
.spec{font-weight:700;font-size:11.5px;color:var(--purple);line-height:1.25}
.phone-pill{display:inline-flex;align-items:center;gap:8px;margin-top:12px;background:var(--sky);border-radius:14px;padding:4px 14px;font-weight:700;font-size:12px;color:#234}
.phone-pill svg{width:12px;height:12px}
/* inside */
.what{position:absolute;left:24px;top:250px;width:332px}
.h-purple{font-weight:700;font-size:12.5px;color:var(--purple);margin-bottom:5px}
.body{font-size:9px;line-height:1.38}
.ticks{list-style:none;margin-top:8px}
.ticks h5{font-size:10px;margin-bottom:4px;color:#333}
.ticks li{font-size:9.5px;display:flex;align-items:center;gap:7px;margin-bottom:3px}
.ticks li svg{width:10px;height:10px;flex:0 0 10px}
.middle{position:absolute;left:26px;top:40px;width:330px}
.middle .h-purple{color:#333;font-size:12px}
.middle section{margin-bottom:14px}
.dots{list-style:none}
.dots li{font-size:9px;line-height:1.35;padding-left:13px;position:relative;margin-bottom:4px}
.dots li::before{content:"";position:absolute;left:0;top:3px;width:6px;height:6px;border-radius:50%;border:1.5px solid var(--blue)}
.web{position:absolute;left:0;right:0;bottom:22px;text-align:center;font-size:10px;letter-spacing:3px;color:#333}
.bio{position:absolute;left:24px;top:28px;width:332px}
.bio h3{font-weight:700;font-size:12px;color:var(--purple);margin-bottom:4px}
.bio .logo{position:absolute;left:110px;top:190px}
.bio-foot{position:absolute;left:0;right:0;bottom:20px;text-align:center}
.bio-foot .phone{font-weight:700;font-size:22px;color:var(--teal);display:inline-flex;align-items:center;gap:8px}
.bio-foot .phone svg{width:18px;height:18px}
.bio-foot .site{font-size:10px;letter-spacing:3px;color:#333;margin-top:4px}
</style>
</head>
<body>

<!-- OUTSIDE SPREAD -->
<div class="spread spread--outside">

  <div class="panel panel--1">
    <div class="photo" role="img" aria-label="Green bamboo stalks reflected in calm water" style="left:0;bottom:0;width:170px;height:200px;background:radial-gradient(ellipse at 30% 60%,#7fbf3a 0%,#b5da6a 45%,rgba(255,255,255,0) 75%)"></div>
    <div class="services">
      <div class="h-caps">PSYCHOLOGICAL SERVICES</div>
      <div class="service"><span class="service__icon"></span><div><h4>Initial evaluation</h4><p>Mental health assessment, diagnosis and comprehensive wellness planning.</p></div></div>
      <div class="service"><span class="service__icon"></span><div><h4>Gentle Horizon Therapy</h4><p>Resolve emotional distress, heartbreak and grief. It clears trauma at the subconscious level with hypnotic communication. The most troubling memories are worked through and clients gain a sense of clarity, peace and power. Only a couple of sessions are needed to experience dramatic and long-lasting effects.</p></div></div>
      <div class="service"><span class="service__icon"></span><div><h4>Eye Movement Desensitization &amp; Reprocessing (EMDR)</h4><p>Evidence-based treatment for post-traumatic stress disorder, anxiety, depression and adverse experiences. Experience relief and empowerment. More information is available at our office.</p></div></div>
      <div class="service"><span class="service__icon"></span><div><h4>Short-term talk therapy</h4><p>Psychotherapy to create a more satisfying life. Proactive approach to seeking effective solutions for your most pressing emotional and relational problems.</p></div></div>
      <div class="service"><span class="service__icon"></span><div><h4>Meditation for Wellness</h4><p>Personalized meditation for calm, healing and well-being.</p></div></div>
      <p class="fee"><b>Fee Information:</b><strong>Statewide and Veterans plans accepted and filed.</strong></p>
    </div>
  </div>

  <div class="panel panel--2">
    <svg class="bg" viewBox="0 0 380 555" preserveAspectRatio="none">
      <defs><linearGradient id="g2" x1="0" y1="0" x2="1" y2="1"><stop offset="0" stop-color="#cadf82"/><stop offset=".55" stop-color="#abd037"/><stop offset="1" stop-color="#8fbf2a"/></linearGradient></defs>
      <path d="M380 0 V555 H210 C100 540 30 470 40 380 C50 300 100 260 80 200 C60 130 110 40 200 0 Z" fill="url(#g2)"/>
      <path d="M210 555 C100 540 30 470 40 380 C50 300 100 260 80 200" fill="none" stroke="var(--sky)" stroke-width="4"/>
      <path d="M380 0 C330 30 300 60 300 60" fill="none" stroke="var(--sky)" stroke-width="3"/>
      <circle cx="195" cy="140" r="92" fill="#fff"/>
    </svg>
    <div class="layer">
      <div class="logo" style="position:absolute;left:120px;top:22px"><span class="logo__dot"></span><span class="logo__name">STILLWATER<small>holistic wellness center</small></span></div>
      <div class="photo" role="img" aria-label="Clear turquoise ocean water with gentle ripples" style="left:111px;top:56px;width:168px;height:168px;border-radius:50%;background:radial-gradient(circle at 40% 35%,#9fe3ef,#3bb4d0 60%,#1f8fb8)"></div>
      <div class="back-text">
        <div class="name-line">Marianne Dobbs, Psy.D.</div>
        <div class="role-line">Licensed Psychologist</div>
        <div class="mantra">Heal the Past<br>Embrace the Present<br>Create the Future</div>
        <div class="contact">
          <svg class="icon" viewBox="0 0 14 14"><circle cx="7" cy="7" r="7" fill="var(--blue)"/><path d="M3.5 7.5 L7 4.2 L10.5 7.5 M4.8 7 V10 H9.2 V7" fill="none" stroke="#fff" stroke-width="1.2"/></svg>
          <b>Harbor Plaza</b><br>210 Seaside Rd #14<br>Coral Bay, FL 30012
          <svg class="icon" viewBox="0 0 14 14"><circle cx="7" cy="7" r="7" fill="var(--blue)"/><path d="M4.5 4 C4.5 7.5 6.5 9.5 10 9.5 L10 8.3 L8.6 7.8 L8 8.5 C7 8 6 7 5.5 6 L6.2 5.4 L5.7 4 Z" fill="#fff"/></svg>
          <b>555 014-2290</b>
          <svg class="icon" viewBox="0 0 14 14"><circle cx="7" cy="7" r="7" fill="var(--blue)"/><circle cx="7" cy="7" r="3.8" fill="none" stroke="#fff"/><path d="M3.2 7 H10.8 M7 3.2 C5 5 5 9 7 10.8 M7 3.2 C9 5 9 9 7 10.8" fill="none" stroke="#fff" stroke-width=".8"/></svg>
          www.stillwaterhwc.com
        </div>
      </div>
    </div>
  </div>

  <div class="panel panel--3">
    <svg class="bg" viewBox="0 0 380 555" preserveAspectRatio="none">
      <defs>
        <linearGradient id="g3" x1="0" y1="0" x2="0" y2="1"><stop offset="0" stop-color="#ffffff"/><stop offset=".35" stop-color="#e5f0bf"/><stop offset=".7" stop-color="#abd037"/><stop offset="1" stop-color="#8fbf2a"/></linearGradient>
      </defs>
      <rect width="380" height="555" fill="url(#g3)"/>
      <path d="M380 150 C300 220 260 300 270 400 C280 480 320 530 360 555 H380 Z" fill="var(--sky)" opacity=".8"/>
      <path d="M0 520 C60 480 120 460 190 470" fill="none" stroke="var(--sky)" stroke-width="3"/>
    </svg>
    <div class="photo" role="img" aria-label="Purple lotus flower on green lily pads" style="left:70px;top:300px;width:310px;height:255px;border-top-left-radius:160px 140px;background:radial-gradient(circle at 45% 45%,#f2d13a 0 6%,#9a7ad0 12%,#7a5bbf 28%,#4f8f2a 42%,#3f7a22 70%)"></div>
    <div class="cover-text">
      <div class="logo"><span class="logo__dot"></span><span class="logo__name">STILLWATER<small>holistic wellness center</small></span></div>
      <div class="name-line" style="font-size:16px">Marianne Dobbs, Psy.D.</div>
      <div class="tagline"><span>LIVE WELL, LOVE WELL</span><span>LICENSED PSYCHOLOGIST</span></div>
      <div class="subline">Unleashing the Power of the Mind<br>for Healing and Well-being</div>
      <div class="script">Specializing in</div>
      <div class="spec">Adults &amp; Gentle Horizon<br>Therapy</div>
      <div class="phone-pill"><svg viewBox="0 0 14 14"><path d="M2 1.5 C2 8 6 12 12.5 12 L12.5 9.6 L9.8 8.6 L8.6 10 C6.6 9 5 7.4 4 5.4 L5.4 4.2 L4.4 1.5 Z" fill="#1f5f7a"/></svg>555 014-2290</div>
    </div>
  </div>
</div>

<!-- INSIDE SPREAD -->
<div class="spread spread--inside">

  <div class="panel panel--1">
    <svg class="bg" viewBox="0 0 380 555" preserveAspectRatio="none">
      <defs><linearGradient id="g4" x1="0" y1="0" x2="1" y2="1"><stop offset="0" stop-color="#abd037"/><stop offset=".6" stop-color="#cadf82"/><stop offset="1" stop-color="#ffffff"/></linearGradient></defs>
      <path d="M0 0 H380 V200 C300 230 200 250 120 235 C60 225 20 230 0 240 Z" fill="url(#g4)"/>
      <path d="M0 250 C40 238 90 236 140 244" fill="none" stroke="var(--sky)" stroke-width="3"/>
      <circle cx="150" cy="122" r="104" fill="#fff"/>
    </svg>
    <div class="photo" role="img" aria-label="Dandelion seed head against a blue sky" style="left:54px;top:26px;width:192px;height:192px;border-radius:50%;background:radial-gradient(circle at 50% 50%,#eef3f6 0 18%,#7fb4dd 40%,#2f6fb8 80%)"></div>
    <div class="what">
      <div class="h-purple">What is Gentle Horizon Therapy?</div>
      <p class="body">This therapy dramatically enhances mood, creates calm, eases grief, optimizes health and promotes success. It is a form of hypnosis that clears stuck patterns of thinking and feeling at the subconscious level. Past emotionally charged memories are cleared. You do not have to talk about problems, share scattered thoughts, cry nor re-experience uncomfortable emotions. You are guided to engage in deep brain processing to create an internal shift for automatic changes in thoughts, feelings and behaviors. Profound change happens within your nervous system, facilitating lasting positive effects. Only one or two sessions are needed to experience immediate symptom relief.</p>
      <ul class="ticks">
        <h5>It is effective for many of life's problems including:</h5>
        <li><svg viewBox="0 0 10 10"><circle cx="5" cy="5" r="5" fill="var(--sky)"/><path d="M2.6 5 L4.3 6.7 L7.4 3.4" fill="none" stroke="#fff" stroke-width="1.3"/></svg>PTSD, Sexual Abuse and Childhood Abuse</li>
        <li><svg viewBox="0 0 10 10"><circle cx="5" cy="5" r="5" fill="var(--sky)"/><path d="M2.6 5 L4.3 6.7 L7.4 3.4" fill="none" stroke="#fff" stroke-width="1.3"/></svg>Grief, Infidelity and Heartbreak</li>
        <li><svg viewBox="0 0 10 10"><circle cx="5" cy="5" r="5" fill="var(--sky)"/><path d="M2.6 5 L4.3 6.7 L7.4 3.4" fill="none" stroke="#fff" stroke-width="1.3"/></svg>Relationship issues</li>
        <li><svg viewBox="0 0 10 10"><circle cx="5" cy="5" r="5" fill="var(--sky)"/><path d="M2.6 5 L4.3 6.7 L7.4 3.4" fill="none" stroke="#fff" stroke-width="1.3"/></svg>Anger and Resentment</li>
        <li><svg viewBox="0 0 10 10"><circle cx="5" cy="5" r="5" fill="var(--sky)"/><path d="M2.6 5 L4.3 6.7 L7.4 3.4" fill="none" stroke="#fff" stroke-width="1.3"/></svg>Guilt / Shame</li>
        <li><svg viewBox="0 0 10 10"><circle cx="5" cy="5" r="5" fill="var(--sky)"/><path d="M2.6 5 L4.3 6.7 L7.4 3.4" fill="none" stroke="#fff" stroke-width="1.3"/></svg>Anxiety / Fear</li>
        <li><svg viewBox="0 0 10 10"><circle cx="5" cy="5" r="5" fill="var(--sky)"/><path d="M2.6 5 L4.3 6.7 L7.4 3.4" fill="none" stroke="#fff" stroke-width="1.3"/></svg>Nightmares / Insomnia</li>
        <li><svg viewBox="0 0 10 10"><circle cx="5" cy="5" r="5" fill="var(--sky)"/><path d="M2.6 5 L4.3 6.7 L7.4 3.4" fill="none" stroke="#fff" stroke-width="1.3"/></svg>Stress-related symptoms and Pain</li>
      </ul>
    </div>
  </div>

  <div class="panel panel--2">
    <svg class="bg" viewBox="0 0 380 555" preserveAspectRatio="none">
      <rect width="380" height="555" fill="#bfe4f4"/>
      <path d="M0 0 H380 V20 C250 40 120 30 0 60 Z" fill="#fff"/>
      <path d="M380 380 C340 440 320 500 330 555 H380 Z" fill="#fff"/>
    </svg>
    <div class="middle">
      <section>
        <div class="h-purple">Clearing old stuff and making way for new beginnings</div>
        <p class="body">If you have been unable to change how you feel, think or act, it is likely that you are being affected by experiences from your past. When something is painful or disturbing, it slams into awareness and leaves a lasting impression. Even when the experience is finished, deeper parts of the mind may continue to respond as if the disturbing event is still occurring. When fueled by the ongoing influence of past events, emotional problems, destructive behaviors and relationship difficulties are impossible to overcome. You may consciously understand the value of change, yet change is not likely unless your deeper mind is engaged. In this therapy the subconscious mind is transformed, and the influence of past events is eliminated.</p>
      </section>
      <section>
        <div class="h-purple">What happens in a session?</div>
        <p class="body">Trauma is stored in the mind and body. In a session you will experience profound physiological calm and you will be guided toward emotional resolution in a gentle, creative and even humorous way. You access inner resources of light, wisdom and peace. As Elias Moore states, "we all have a true self within, we just sometimes forget it is there." From this place, painful emotional memories are easily reframed with new meaning. You will leave the session feeling peaceful and sourced from within by a free-flowing energy.</p>
      </section>
      <section>
        <div class="h-purple">Clear Your Mind and Change Your World</div>
        <ul class="dots">
          <li>Discover and resolve subconscious causes for emotional and behavioral difficulties</li>
          <li>Eliminate unconscious conflicts blocking desired change</li>
          <li>Promote mind / body healing</li>
        </ul>
      </section>
    </div>
    <div class="web">www.stillwaterhwc.com</div>
  </div>

  <div class="panel panel--3">
    <svg class="bg" viewBox="0 0 380 555" preserveAspectRatio="none">
      <defs><linearGradient id="g5" x1="0" y1="0" x2="0" y2="1"><stop offset="0" stop-color="#cadf82"/><stop offset="1" stop-color="#abd037"/></linearGradient></defs>
      <path d="M0 450 C80 420 150 360 190 330 C240 290 320 240 380 230 V555 H0 Z" fill="url(#g5)"/>
      <path d="M0 440 C80 410 150 350 190 320" fill="none" stroke="var(--sky)" stroke-width="3"/>
      <circle cx="235" cy="340" r="92" fill="#fff" stroke="var(--lime-soft)" stroke-width="4"/>
    </svg>
    <div class="photo" role="img" aria-label="Portrait of Dr. Marianne Dobbs" style="left:153px;top:258px;width:164px;height:164px;border-radius:50%;background:linear-gradient(180deg,#f4f1ea,#dfe8dc 60%,#a8d8e4)"></div>
    <div class="bio">
      <h3>Dr. Marianne Dobbs</h3>
      <p class="body">Dr. Dobbs is a licensed clinical psychologist specializing in adults and seniors. She treats people for depression, anxiety, grief, sexual trauma, PTSD, relationship issues, infidelity, divorce and stress-related symptoms. She has over 20 years of clinical experience in mental health and is an adjunct counseling professor. She received her master's and doctorate degrees in clinical psychology and a bachelor's degree in rehabilitation. At Stillwater, she provides initial evaluations, assessment, diagnosis and comprehensive treatment planning. She will collaborate with you to create solutions for healing, empowerment and wellness.</p>
      <div class="logo"><span class="logo__dot"></span><span class="logo__name">STILLWATER<small>holistic wellness center</small></span></div>
    </div>
    <div class="bio-foot">
      <div class="phone"><svg viewBox="0 0 14 14"><path d="M2 1.5 C2 8 6 12 12.5 12 L12.5 9.6 L9.8 8.6 L8.6 10 C6.6 9 5 7.4 4 5.4 L5.4 4.2 L4.4 1.5 Z" fill="var(--teal)"/></svg>555 014-2290</div>
      <div class="site">www.stillwaterhwc.com</div>
    </div>
  </div>
</div>

</body>
</html>
```